Letterhead design - Harwick Group

We have just had our Logo created and our now wantng a letterhead design to incorporate this. Please use the same colours as in the logo, which is attached.
Please use the company details below
P O Box 86, Bleneheim 7315
Ph: 03 642 1937
dave@harwickgroup.co.nz
We would like a professional look
We need an overall letterhead design for our varied group of buisinesses which are based in NZ and overseas. We grow and develop buisinesses. Our companies began in NZ but we now have branches overseas as well. People are our greatest asset and we employ some incredible staff. Our buisinesses are scientific, innovative and growing in size and expertise with a financial base.

Target Market(s)

Professionals

Industry/Entity Type

Investment

Requirements
Must have
• Easy to read.
• Please use the same colours as in the logo
• Please use the company details below
• P O Box 86, Bleneheim 7315
• Ph: 03 642 1937
• dave@harwickgroup.co.nz

```html
<!DOCTYPE html>
<html lang="en">
<head>
<meta charset="utf-8">
<title>Harwick Group Letterhead</title>
<link href="https://fonts.googleapis.com/css2?family=Open+Sans:wght@400;600&family=Arimo:wght@400;700&display=swap" rel="stylesheet">
<style>
  :root {
    --brand-green: #25b574;
    --brand-grey: #5a5b5d;
    --ink: #4a4a4a;
    --ink-dark: #222222;
    --rule: #9a9a9a;
    --paper: #ffffff;
    --signature-tone: #d9d9d9;
  }
  html, body { margin: 0; padding: 0; overflow: hidden; background: var(--paper); }
  .letterhead {
    position: relative;
    width: 1040px;
    height: 1200px;
    background: var(--paper);
    font-family: "Open Sans", sans-serif;
    color: var(--ink);
    overflow: hidden;
  }
  .header-band {
    position: absolute;
    top: 0;
    left: 0;
    width: 1040px;
    height: 84px;
    background: linear-gradient(90deg, var(--brand-green) 0%, var(--brand-green) 55%, var(--brand-grey) 100%);
  }
  .brand {
    position: absolute;
    top: 112px;
    left: 614px;
    display: flex;
    align-items: center;
    gap: 14px;
  }
  .brand-square { width: 56px; height: 56px; background: var(--brand-grey); }
  .brand-name {
    font-size: 34px;
    font-weight: 600;
    color: var(--brand-green);
    letter-spacing: 0.5px;
    white-space: nowrap;
  }
  .block { position: absolute; left: 99px; width: 838px; font-size: 16.2px; }
  .issue-date { top: 214px; }
  .recipient { top: 253px; line-height: 19px; }
  .salutation { top: 356px; }
  .body-copy { line-height: 27px; text-align: justify; margin: 0; }
  .para-1 { top: 407px; }
  .para-2 { top: 569px; }
  .para-3 { top: 677px; }
  .closing { top: 812px; }
  .signature {
    position: absolute;
    top: 850px;
    left: 99px;
    width: 240px;
    height: 26px;
    background: linear-gradient(90deg, var(--signature-tone), rgba(217,217,217,0.2));
    border-radius: 4px;
  }
  .signatory-name { top: 886px; font-size: 20px; color: var(--ink-dark); }
  .signatory-title { top: 920px; }
  .footer {
    position: absolute;
    left: 101px;
    width: 838px;
    top: 1114px;
    font-family: "Arimo", sans-serif;
    text-align: center;
    color: var(--ink-dark);
    font-size: 15.5px;
  }
  .footer-rule { height: 1px; background: var(--rule); margin: 8px 0 8px; }
  .contact-label { color: var(--brand-green); font-weight: 700; }
  .contact-sep { margin: 0 14px; color: var(--ink); }
</style>
</head>
<body>
<div class="letterhead">
  <div class="header-band" role="img" aria-label="Decorative green and grey header band"></div>

  <div class="brand">
    <div class="brand-square"></div>
    <div class="brand-name">HARWICK GROUP</div>
  </div>

  <div class="block issue-date">Issuing Date: May 5, 2018</div>
  <div class="block recipient">Name Of Employee Mr. XYZABC<br>Address of Employee<br>Address Line 2 etc..</div>
  <div class="block salutation">Dear Mr.XYZABC</div>

  <p class="block body-copy para-1">Lorem Ipsum has been the industry's standard dummy text ever since the 1500s, when an unknown printer took a galley of type and scrambled it to make a type specimen book. It has survived not only five centuries, but also the leap into electronic typesetting, remaining essentially unchanged. It was popularised in the 1960s with the release of Typeline sheets containing Lorem Ipsum passages, and more recently with desktop publishing software like PageForm Studio including versions of Lorem Ipsum.</p>
  <p class="block body-copy para-2">Lorem Ipsum is simply dummy text of the printing and typesetting industry. Lorem Ipsum has been the industry's standard dummy text ever since the 1500s, when an unknown printer took a galley of type and scrambled it to make a type specimen book.</p>
  <p class="block body-copy para-3">It has survived not only five centuries, but also the leap into electronic typesetting, remaining essentially unchanged. It was popularised in the 1960s with the release of Typeline sheets containing Lorem IpsumIpsum passages.</p>

  <div class="block closing">Yours Sincerely</div>
  <div class="signature" role="img" aria-label="Handwritten signature of Marcus Reid"></div>
  <div class="block signatory-name">Marcus Reid</div>
  <div class="block signatory-title">Managing Director</div>

  <div class="footer">
    <div class="footer-address">P O Box 86, Bleneheim 7315</div>
    <div class="footer-rule"></div>
    <div class="footer-contacts">
      <span class="contact-label">P:</span> 03 642 1937<span class="contact-sep">|</span><span class="contact-label">E:</span> dave@harwickgroup.co.nz
    </div>
  </div>
</div>
</body>
</html>
```